Lip balm label

4 different kinds with a blend of essential oils. Cravings, Energy, Anxiety and Sensual. No preservatives or engineered products. Need different colored labels for each one. Maybe lavender or purple for stress, green or orange for appetite, red for energy and black for sensual. Or just use your professional judgement. Must fit on small lip balm tube

Target Market(s)

Young and old adults

Industry/Entity Type

Cosmetics

Logo Text

Mouthgrove

Logo styles of interest
Wordmark Logo
Font styles to use
Decorative

Requirements
Must have
• Name of company (KoRu Organics), 100% Organic, list of ingredients in each one, weight is 0.15 oz, made with Essential Oils, soothing and moisturizing,
• Lip Balm
Nice to have
• Made in USA, satisfaction guaranteed

```html
<!DOCTYPE html>
<html lang="en">
<head>
<meta charset="utf-8">
<title>Mouthgrove Lip Balm Labels</title>
<link rel="stylesheet" href="https://fonts.googleapis.com/css2?family=PT+Sans&family=PT+Sans+Narrow&family=Arimo:wght@400;700&display=swap">
<style>
  :root {
    --gold: #cdaa6c;
    --paper: #ffffff;
    --sensual: #000000;
    --energy: #9a0e0a;
    --anxiety: #430a48;
  }
  * { margin: 0; padding: 0; box-sizing: border-box; }
  html, body { width: 1200px; height: 1000px; overflow: hidden; background: var(--paper); }
  .sheet { position: relative; width: 1200px; height: 1000px; }

  .label {
    position: absolute; left: 28px; width: 1144px; height: 295px;
    background: var(--label-bg); color: var(--gold);
    border-left: 22px solid var(--gold); border-right: 22px solid var(--gold);
  }
  .label--sensual { top: 22px; --label-bg: var(--sensual); }
  .label--energy  { top: 351px; --label-bg: var(--energy); height: 294px; }
  .label--anxiety { top: 683px; --label-bg: var(--anxiety); }

  .brand {
    position: absolute; left: 100px; top: 62px; width: 360px; text-align: center;
    font-family: "PT Sans Narrow", sans-serif; font-size: 60px; line-height: 1;
  }
  .brand__tagline {
    position: absolute; left: 224px; top: 124px;
    font-family: "PT Sans Narrow", sans-serif; font-size: 24px; line-height: 1;
  }

  .variant {
    position: absolute; left: 540px; width: 400px; top: 62px; text-align: center;
    font-family: "PT Sans Narrow", sans-serif; font-size: 76px; line-height: 1;
  }
  .claim {
    position: absolute; left: 500px; width: 500px; top: 154px; text-align: center;
    font-family: "PT Sans Narrow", sans-serif; font-size: 14px; letter-spacing: 1.2px;
  }

  .maker {
    position: absolute; left: 38px; top: 240px;
    font-family: "PT Sans", sans-serif; font-size: 29px; line-height: 1;
  }
  .ingredients {
    position: absolute; left: 248px; top: 239px; width: 660px;
    font-family: "Arimo", sans-serif; font-size: 12px; line-height: 14.6px;
  }
  .ingredients strong { font-weight: 700; }

  .origin-badge {
    position: absolute; left: 934px; top: 246px; width: 102px; height: 30px;
    border: 1.3px solid var(--gold); border-radius: 15px; text-align: center;
    font-family: "PT Sans", sans-serif; line-height: 1;
  }
  .origin-badge__main { display: block; font-size: 11px; letter-spacing: 0.8px; margin-top: 4px; }
  .origin-badge__sub { display: block; font-size: 7.5px; margin-top: 1px; }

  .weight {
    position: absolute; left: 1078px; top: 250px; width: 0; height: 0;
  }
  .weight span {
    position: absolute; left: 0; top: 0; white-space: nowrap;
    transform: translate(-50%, -50%) rotate(-90deg);
    font-family: "PT Sans", sans-serif; font-size: 17px; letter-spacing: 0.5px;
  }
</style>
</head>
<body>
<main class="sheet">

  <section class="label label--sensual">
    <div class="brand">Mouthgrove</div>
    <div class="brand__tagline">100% Organic Lip Balm</div>
    <h2 class="variant">Sensual</h2>
    <p class="claim">MADE WITH ESSENTIAL OILS, SOOTHING AND MOISTURIZING</p>
    <div class="maker">KoRu Organics</div>
    <p class="ingredients"><strong>100% Organic ingredients:</strong> Lorem ipsum dolor sit amet, consectetur adipiscing elit, sed do eiusmod tempor incidi-dunt ut labore et dolore magna aliqua. Ut enim ad minim veniam, quis nostrud exercitation ullamco laboris nisi ut aliquip ex ea commodo consequat.</p>
    <div class="origin-badge"><span class="origin-badge__main">MADE IN USA</span><span class="origin-badge__sub">Satisfaction guaranteed</span></div>
    <div class="weight"><span>0.15 oz</span></div>
  </section>

  <section class="label label--energy">
    <div class="brand">Mouthgrove</div>
    <div class="brand__tagline">100% Organic Lip Balm</div>
    <h2 class="variant">Energy</h2>
    <p class="claim">MADE WITH ESSENTIAL OILS, SOOTHING AND MOISTURIZING</p>
    <div class="maker">KoRu Organics</div>
    <p class="ingredients"><strong>100% Organic ingredients:</strong> Lorem ipsum dolor sit amet, consectetur adipiscing elit, sed do eiusmod tempor incidi-dunt ut labore et dolore magna aliqua. Ut enim ad minim veniam, quis nostrud exercitation ullamco laboris nisi ut aliquip ex ea commodo consequat.</p>
    <div class="origin-badge"><span class="origin-badge__main">MADE IN USA</span><span class="origin-badge__sub">Satisfaction guaranteed</span></div>
    <div class="weight"><span>0.15 oz</span></div>
  </section>

  <section class="label label--anxiety">
    <div class="brand">Mouthgrove</div>
    <div class="brand__tagline">100% Organic Lip Balm</div>
    <h2 class="variant">Anxiety</h2>
    <p class="claim">MADE WITH ESSENTIAL OILS, SOOTHING AND MOISTURIZING</p>
    <div class="maker">KoRu Organics</div>
    <p class="ingredients"><strong>100% Organic ingredients:</strong> Lorem ipsum dolor sit amet, consectetur adipiscing elit, sed do eiusmod tempor incidi-dunt ut labore et dolore magna aliqua. Ut enim ad minim veniam, quis nostrud exercitation ullamco laboris nisi ut aliquip ex ea commodo consequat.</p>
    <div class="origin-badge"><span class="origin-badge__main">MADE IN USA</span><span class="origin-badge__sub">Satisfaction guaranteed</span></div>
    <div class="weight"><span>0.15 oz</span></div>
  </section>

</main>
</body>
</html>
```